E brochure for company overview

We need a brochure for a company overview that will be sent to potential new clients. We are uploading a file with all the content that needs to be included inside of the brochure. We need this content to be displayed in a professional, neat, and creative way. The file has a Spanish and English version so we need two versions of the brochure in each language. *This brochure will be viewed digitally and it will not be printed, thus it does not need a cover page*. We included our company logo (Parvolux) Please utilize this in your design.

```html
<!DOCTYPE html>
<html lang="en">
<head>
<meta charset="utf-8">
<title>Parvolux – Company Overview (English / Español)</title>
<link href="https://fonts.googleapis.com/css2?family=Roboto+Condensed:wght@400;700&display=swap" rel="stylesheet">
<style>
  :root{
    --orange:#f26a21;
    --orange-light:#f7953a;
    --red:#e4322b;
    --ink:#1f1f1f;
    --ink-soft:#333;
    --rule:#9a9a9a;
    --white:#ffffff;
    --backdrop:#eceef2;
    --hero-dark:#0e1f33;
    --hero-mid:#1f4a6e;
  }
  *{box-sizing:border-box;margin:0;padding:0}
  html,body{width:800px;height:1200px;overflow:hidden;background:var(--backdrop)}
  body{font-family:"Roboto Condensed",Arial,sans-serif;color:var(--ink)}

  .spread{position:relative;width:800px;height:1200px}

  .page{position:absolute;left:184px;width:432px;height:576px;background:var(--white);overflow:hidden;
    box-shadow:0 6px 18px rgba(0,0,0,.18)}
  .page-en{top:16px}
  .page-es{top:608px}

  .hero{position:absolute;left:0;top:0;width:432px;height:225px;
    background:
      radial-gradient(circle at 42% 60%, #f7a53a 0, rgba(247,165,58,.55) 5%, rgba(63,169,214,.35) 18%, rgba(31,74,110,0) 42%),
      radial-gradient(ellipse at 28% 85%, rgba(63,169,214,.6) 0, rgba(63,169,214,0) 45%),
      linear-gradient(135deg,var(--hero-mid) 0%,var(--hero-dark) 55%,#1b2a3a 100%);}

  .brand-tab{position:absolute;left:112px;top:0;width:208px;height:50px;background:var(--white);
    border-radius:0 0 16px 16px;display:flex;align-items:center;justify-content:center;gap:8px;
    box-shadow:0 3px 8px rgba(0,0,0,.25)}
  .brand-dot{width:20px;height:20px;border-radius:50%;background:var(--red)}
  .brand-text{display:flex;flex-direction:column;line-height:1}
  .brand-name{font-size:23px;font-weight:700;color:var(--ink);letter-spacing:.3px}
  .brand-tag{font-size:7.5px;color:var(--ink-soft);letter-spacing:.5px;margin-top:2px}

  .columns{position:absolute;left:20px;top:235px;width:392px;height:228px}
  .divider-v{position:absolute;left:194px;top:0;height:226px;border-left:1px dotted var(--rule)}
  .divider-h{position:absolute;border-top:1px dotted var(--rule)}
  .divider-left{left:0;top:104px;width:188px}
  .divider-right{left:202px;top:98px;width:190px}

  .block{position:absolute}
  .history{left:4px;top:8px;width:182px}
  .vision{left:4px;top:112px;width:182px}
  .mission{left:204px;top:0;width:186px}
  .services{left:204px;top:104px;width:186px}

  .block-head{display:flex;align-items:center;gap:9px;margin-bottom:4px}
  .icon{width:32px;height:32px;border-radius:50%;flex:none;
    background:radial-gradient(circle at 35% 30%,var(--orange-light),var(--orange) 55%,var(--red));
    box-shadow:0 2px 4px rgba(0,0,0,.25);display:flex;align-items:center;justify-content:center}
  .icon svg{width:17px;height:17px}
  .block-title{font-size:12px;font-weight:700;color:var(--ink);letter-spacing:.2px;line-height:1.1}
  .block-text{font-size:8.5px;line-height:1.3;color:var(--ink-soft);text-align:justify}
  .block-text strong{display:block;font-size:9.5px;color:var(--ink)}

  .values-label{font-size:8.5px;color:var(--ink-soft);margin-top:3px}
  .values{list-style:none;display:grid;grid-template-columns:1fr 1fr 1fr;gap:3px 6px;margin-top:3px}
  .values li{font-size:8px;line-height:1.2;color:var(--ink-soft);display:flex;align-items:flex-start;gap:3px}
  .values li::before{content:"";flex:none;margin-top:2px;width:0;height:0;
    border-left:5px solid var(--orange);border-top:3px solid transparent;border-bottom:3px solid transparent}

  .partners{position:absolute;left:20px;top:476px;width:392px;height:64px;
    border:1px solid #bdbdbd;border-radius:12px;background:var(--white)}
  .partners-label{position:absolute;left:146px;top:-11px;height:22px;padding:0 16px;border-radius:11px;
    background:linear-gradient(90deg,var(--red),var(--orange));color:var(--white);
    font-size:11px;font-weight:700;display:flex;align-items:center;letter-spacing:.3px}
  .partner-list{position:absolute;left:0;right:0;top:20px;display:flex;justify-content:space-around;align-items:center;list-style:none}
  .partner-list li{font-size:15px;font-weight:700;color:var(--ink-soft)}

  .footer{position:absolute;left:0;bottom:0;width:432px;height:30px;
    background:linear-gradient(90deg,var(--red),var(--orange) 60%,var(--red));
    display:flex;align-items:center;justify-content:space-around;color:var(--white)}
  .contact{display:flex;align-items:center;gap:5px;font-size:10px;font-weight:700}
  .contact-icon{width:15px;height:15px;border-radius:50%;border:1px solid var(--white);display:flex;align-items:center;justify-content:center}
  .contact-icon svg{width:8px;height:8px}
</style>
</head>
<body>
<main class="spread">

  <!-- English version -->
  <article class="page page-en" lang="en">
    <div class="hero" role="img" aria-label="Photo of a hand touching a glowing digital network above a circuit interface"></div>

    <header class="brand-tab">
      <span class="brand-dot"></span>
      <div class="brand-text">
        <span class="brand-name">PARVOLUX</span>
        <span class="brand-tag">IT CONSULTING AND SERVICES</span>
      </div>
    </header>

    <section class="columns">
      <div class="divider-v"></div>
      <div class="divider-h divider-left"></div>
      <div class="divider-h divider-right"></div>

      <div class="block history">
        <div class="block-head">
          <span class="icon"><svg viewBox="0 0 34 34" fill="none" stroke="#fff" stroke-width="3"><circle cx="17" cy="17" r="12"/><path d="M17 10v7l5 4"/></svg></span>
          <h2 class="block-title">HISTORY:</h2>
        </div>
        <p class="block-text"><strong>Parvolux initiates on 2006</strong>Parvolux has 15 years in the technology industry, specialising in security management, infrastructure and service management.</p>
      </div>

      <div class="block vision">
        <div class="block-head">
          <span class="icon"><svg viewBox="0 0 38 26" fill="none" stroke="#fff" stroke-width="3"><path d="M2 13C8 4 30 4 36 13C30 22 8 22 2 13Z"/><circle cx="19" cy="13" r="5"/></svg></span>
          <h2 class="block-title">VISION:</h2>
        </div>
        <p class="block-text">To be recognized by our customers as an important company in the Dominican Republic in the area of security and infrastructure and achieve presence throughout the Caribbean and Central America.</p>
      </div>

      <div class="block mission">
        <div class="block-head">
          <span class="icon"><svg viewBox="0 0 34 34" fill="none" stroke="#fff" stroke-width="3"><circle cx="17" cy="17" r="13"/><circle cx="17" cy="17" r="7"/><circle cx="17" cy="17" r="1.5" fill="#fff"/></svg></span>
          <h2 class="block-title">MISSION:</h2>
        </div>
        <p class="block-text">Providing our customers with the best human and technological resources with the clear objective of providing effective solutions using best industry practices.</p>
      </div>

      <div class="block services">
        <div class="block-head">
          <span class="icon"><svg viewBox="0 0 34 34" fill="none" stroke="#fff" stroke-width="3"><circle cx="17" cy="17" r="6"/><path d="M17 3v5M17 26v5M3 17h5M26 17h5M7 7l4 4M23 23l4 4M27 7l-4 4M11 23l-4 4"/></svg></span>
          <h2 class="block-title">OUR SERVICES:</h2>
        </div>
        <p class="block-text">Service Management, Security of information, Custom development, Device and network monitoring, Devops, API management, Staffing</p>
        <p class="values-label">Values</p>
        <ul class="values">
          <li>Integrity</li><li>Team Work</li><li>Positive Attitude</li>
          <li>Creativity</li><li>Commitment</li>
        </ul>
      </div>
    </section>

    <section class="partners">
      <h2 class="partners-label">OUR PARTNERS:</h2>
      <ul class="partner-list">
        <li>CORVANE</li><li>lumetra</li><li>taskhaven</li><li>helio</li>
      </ul>
    </section>

    <footer class="footer">
      <span class="contact"><span class="contact-icon"><svg viewBox="0 0 16 16"><path d="M3 1l3 3-2 2c1 2 3 4 5 5l2-2 3 3-2 3C6 15 1 10 1 3Z" fill="#fff"/></svg></span>809 555 0142</span>
      <span class="contact"><span class="contact-icon"><svg viewBox="0 0 16 16" fill="none" stroke="#fff" stroke-width="1.5"><circle cx="8" cy="8" r="6.5"/><path d="M1.5 8h13M8 1.5c-3 3-3 10 0 13M8 1.5c3 3 3 10 0 13"/></svg></span>www.parvolux.com.do</span>
      <span class="contact"><span class="contact-icon"><svg viewBox="0 0 16 12" fill="none" stroke="#fff" stroke-width="1.5"><rect x="1" y="1" width="14" height="10"/><path d="M1 1l7 6 7-6"/></svg></span>info@parvolux.com</span>
    </footer>
  </article>

  <!-- Spanish version -->
  <article class="page page-es" lang="es">
    <div class="hero" role="img" aria-label="Foto de una mano tocando una red digital luminosa sobre una interfaz de circuitos"></div>

    <header class="brand-tab">
      <span class="brand-dot"></span>
      <div class="brand-text">
        <span class="brand-name">PARVOLUX</span>
        <span class="brand-tag">IT CONSULTING AND SERVICES</span>
      </div>
    </header>

    <section class="columns">
      <div class="divider-v"></div>
      <div class="divider-h divider-left"></div>
      <div class="divider-h divider-right"></div>

      <div class="block history">
        <div class="block-head">
          <span class="icon"><svg viewBox="0 0 34 34" fill="none" stroke="#fff" stroke-width="3"><circle cx="17" cy="17" r="12"/><path d="M17 10v7l5 4"/></svg></span>
          <h2 class="block-title">HISTORIA:</h2>
        </div>
        <p class="block-text"><strong>Parvolux inicia en 2006</strong>Parvolux tiene 15 años en la industria de la tecnología, especializándose en administración de seguridad, infraestructura y administración de servicios.</p>
      </div>

      <div class="block vision">
        <div class="block-head">
          <span class="icon"><svg viewBox="0 0 38 26" fill="none" stroke="#fff" stroke-width="3"><path d="M2 13C8 4 30 4 36 13C30 22 8 22 2 13Z"/><circle cx="19" cy="13" r="5"/></svg></span>
          <h2 class="block-title">VISIÓN:</h2>
        </div>
        <p class="block-text">Ser reconocidos por nuestros clientes como una empresa importante en República Dominicana en el área de seguridad e infraestructura y lograr presencia en todo el Caribe y Centroamérica.</p>
      </div>

      <div class="block mission">
        <div class="block-head">
          <span class="icon"><svg viewBox="0 0 34 34" fill="none" stroke="#fff" stroke-width="3"><circle cx="17" cy="17" r="13"/><circle cx="17" cy="17" r="7"/><circle cx="17" cy="17" r="1.5" fill="#fff"/></svg></span>
          <h2 class="block-title">MISIÓN:</h2>
        </div>
        <p class="block-text">Brindar a nuestros clientes los mejores recursos humanos y tecnológicos con el claro objetivo de brindar soluciones efectivas utilizando las mejores prácticas de la industria.</p>
      </div>

      <div class="block services">
        <div class="block-head">
          <span class="icon"><svg viewBox="0 0 34 34" fill="none" stroke="#fff" stroke-width="3"><circle cx="17" cy="17" r="6"/><path d="M17 3v5M17 26v5M3 17h5M26 17h5M7 7l4 4M23 23l4 4M27 7l-4 4M11 23l-4 4"/></svg></span>
          <h2 class="block-title">NUESTROS<br>SERVICIOS:</h2>
        </div>
        <p class="block-text">Gestión de servicios, Seguridad de la información, Desarrollo personalizado, Monitorización de dispositivos y redes, Devops, Gestión de API, Staffing</p>
        <ul class="values">
          <li>Integridad</li><li>Actitud positiva</li><li>Trabajo en equipo</li>
          <li>Creatividad</li><li>Compromiso</li>
        </ul>
      </div>
    </section>

    <section class="partners">
      <h2 class="partners-label">OUR PARTNERS:</h2>
      <ul class="partner-list">
        <li>CORVANE</li><li>lumetra</li><li>taskhaven</li><li>helio</li>
      </ul>
    </section>

    <footer class="footer">
      <span class="contact"><span class="contact-icon"><svg viewBox="0 0 16 16"><path d="M3 1l3 3-2 2c1 2 3 4 5 5l2-2 3 3-2 3C6 15 1 10 1 3Z" fill="#fff"/></svg></span>809 555 0142</span>
      <span class="contact"><span class="contact-icon"><svg viewBox="0 0 16 16" fill="none" stroke="#fff" stroke-width="1.5"><circle cx="8" cy="8" r="6.5"/><path d="M1.5 8h13M8 1.5c-3 3-3 10 0 13M8 1.5c3 3 3 10 0 13"/></svg></span>www.parvolux.com.do</span>
      <span class="contact"><span class="contact-icon"><svg viewBox="0 0 16 12" fill="none" stroke="#fff" stroke-width="1.5"><rect x="1" y="1" width="14" height="10"/><path d="M1 1l7 6 7-6"/></svg></span>info@parvolux.com</span>
    </footer>
  </article>

</main>
</body>
</html>
```